Business Card for a Jewellery Brand

Business card for an upscale jewellery brand. Attached is the brand logo and icon and color board. I am looking for two card versions: one for the founder and one is generic. The card should be elegant and convey upscale and premium feel. I am open to both square and rectangle card shapes.

Industry/Entity Type

Jewelry

Contact Information for Business Card

Two cards: (1) Sunila Perumbadi (Founder) (2) General
(1) Sunila Perumbadi card should have Name: Sunila Perumbadi, Title: Founder Email id: sunila@quelm.com.au. Phone no: +61412555307
(2) Generic card should have Email id: info@quelm.com.au. Phone no: +61431555962

Requirements
Must have
• Workmark
• ICON
• Phone no
• Email ID
• ABN: 48917205563 (Note: ABN is Business number in Australia)
• Website: www.quelm.com.au
• Instagram: quelm_jewellery
• Facebook: @quelmjewellery
Nice to have
• Tagline

```html
<!DOCTYPE html>
<html lang="en">
<head>
<meta charset="utf-8">
<title>QUELM Business Card</title>
<link href="https://fonts.googleapis.com/css2?family=Open+Sans:wght@300;400;600&display=swap" rel="stylesheet">
<style>
  :root {
    --bg: #ebe8e5;
    --card-dark: #343334;
    --card-pink: #f0a8a4;
    --rose-gold: #f2a9a2;
    --silver: #dcdcdc;
    --silver-deep: #b9b9bb;
    --ink-light: #f6f6f6;
  }
  * { margin: 0; padding: 0; box-sizing: border-box; }
  html, body {
    width: 1200px; height: 800px; overflow: hidden;
    background: var(--bg);
    font-family: "Open Sans", Arial, sans-serif;
  }
  .stage {
    width: 1200px; height: 800px;
    display: flex; align-items: center; justify-content: center; gap: 50px;
  }
  .card {
    width: 530px; height: 324px;
    border-radius: 22px;
    position: relative;
    box-shadow: 0 6px 18px rgba(0,0,0,0.14);
  }
  .card-front { background: var(--card-dark); }
  .card-back { background: var(--card-pink); }

  /* Front */
  .front-brand {
    position: absolute; inset: 0;
    display: flex; flex-direction: column; align-items: center; justify-content: center;
  }
  .wordmark {
    font-weight: 300; letter-spacing: 0.28em;
    color: var(--rose-gold); font-size: 64px; line-height: 1;
    padding-left: 0.28em;
  }
  .tagline {
    margin-top: 14px;
    font-size: 15px; letter-spacing: 0.06em; color: var(--silver);
    font-weight: 400;
  }

  /* Back */
  .back-wordmark {
    position: absolute; top: 30px; right: 34px;
    font-weight: 300; letter-spacing: 0.24em; font-size: 40px;
    color: var(--silver); line-height: 1;
  }
  .website {
    position: absolute; top: 150px; right: 34px;
    font-size: 12px; color: var(--silver); letter-spacing: 0.02em;
  }
  .person {
    position: absolute; left: 30px; top: 96px;
    padding-left: 16px; border-left: 7px solid var(--ink-light);
  }
  .person-name { font-size: 21px; font-weight: 600; color: var(--silver); line-height: 1.15; }
  .person-role { font-size: 13px; color: var(--silver); margin-top: 2px; }
  .contacts {
    position: absolute; left: 53px; top: 176px;
    list-style: none; font-size: 14px; color: var(--silver);
  }
  .contacts li { display: flex; align-items: center; gap: 8px; height: 24px; }
  .contacts .abn { margin-bottom: 4px; }
  .icon { width: 14px; height: 14px; flex: none; }
  .icon-plain { width: 13px; height: 13px; background: var(--silver-deep); border-radius: 2px; flex: none; }
</style>
</head>
<body>
<main class="stage">
  <section class="card card-front" aria-label="Card front">
    <div class="front-brand">
      <div class="wordmark">QUELM</div>
      <div class="tagline">EXQUISITE SILVER JEWELLERY</div>
    </div>
  </section>

  <section class="card card-back" aria-label="Card back">
    <div class="back-wordmark">QUELM</div>
    <div class="website">www.quelm.com.au</div>

    <div class="person">
      <div class="person-name">Sunila Perumbadi</div>
      <div class="person-role">Founder</div>
    </div>

    <ul class="contacts">
      <li class="abn">ABN: 48917205563</li>
      <li>
        <svg class="icon" viewBox="0 0 14 14" aria-hidden="true">
          <rect x="1" y="3" width="12" height="8" fill="none" stroke="#dcdcdc" stroke-width="1.3"/>
          <path d="M1 3 L7 8 L13 3" fill="none" stroke="#dcdcdc" stroke-width="1.3"/>
        </svg>
        sunila@quelm.com.au
      </li>
      <li>
        <svg class="icon" viewBox="0 0 14 14" aria-hidden="true">
          <path d="M3 1.5 L5.5 1.5 L6.3 4.5 L4.8 5.6 Q6 8.3 8.4 9.3 L9.5 7.8 L12.5 8.6 L12.5 11 Q12 12.5 10.5 12.5 Q2 11.5 1.5 3 Q1.5 1.5 3 1.5 Z" fill="#dcdcdc"/>
        </svg>
        +61412555307
      </li>
      <li><span class="icon-plain"></span>quelm_jewellery</li>
      <li><span class="icon-plain"></span>@quelmjewellery</li>
    </ul>
  </section>
</main>
</body>
</html>
```